Fresh Start Body Quest 2017 Poster

We are having a Fresh Start, Body Quest for 2017 at our fitness studio. We need a poster design using the template attached as a reference (Only reference). I have also included our Drovelux logo to put on the poster. Please DO NOT use the graphics in the flyer as we are expecting something much much better :-)
MUST HAVES:
- Size needed 11x17 with bleeding for printing
- .PSD File Format WITH LAYERS (CS3 Compatible)*** A MUST
- Use Drovelux Bootcamps Logo
- Use Information in the attached word doc

```html
<!DOCTYPE html>
<html lang="en">
<head>
<meta charset="utf-8">
<title>Fresh Start Body Quest 2017 Poster</title>
<link rel="stylesheet" href="https://fonts.googleapis.com/css2?family=Libre+Baskerville:wght@700&family=Oxygen:wght@300;400;700&display=swap">
<style>
  :root {
    --backdrop: #d9d4cd;
    --poster-dark: #262627;
    --gold: #b3731f;
    --blue: #2f63ae;
    --blue-deep: #22509a;
    --gray-top: #5b5b5e;
    --gray-bottom: #2c2c2e;
    --ink: #1c1c1d;
    --white: #ffffff;
  }
  html, body {
    margin: 0;
    width: 1200px;
    height: 1200px;
    overflow: hidden;
    background: var(--backdrop);
  }
  .poster {
    position: absolute;
    left: 231px;
    top: 30px;
    width: 737px;
    height: 1140px;
    background: var(--poster-dark);
    overflow: hidden;
    box-shadow: 0 6px 18px rgba(0,0,0,0.3);
  }
  .brand-name {
    position: absolute;
    top: 44px;
    left: 0;
    width: 100%;
    text-align: center;
    font-family: "Oxygen", sans-serif;
    font-weight: 700;
    font-size: 38px;
    letter-spacing: 1px;
    color: #ecebe8;
  }
  .headline {
    position: absolute;
    left: 0;
    width: 100%;
    text-align: center;
    font-family: "Libre Baskerville", serif;
    font-weight: 700;
    color: var(--gold);
    margin: 0;
    line-height: 1;
    text-transform: uppercase;
  }
  .headline-top { top: 124px; font-size: 60px; }
  .headline-bottom { top: 190px; font-size: 48px; letter-spacing: 2px; }
  .hero {
    position: absolute;
    left: 0;
    top: 256px;
    width: 737px;
    height: 490px;
  }
  .info {
    position: absolute;
    left: 0;
    top: 746px;
    width: 100%;
    height: 394px;
    background: linear-gradient(var(--gray-top), var(--gray-bottom));
  }
  .offer {
    position: absolute;
    left: 0;
    width: 100%;
    text-align: center;
    font-family: "Oxygen", sans-serif;
    font-weight: 400;
    color: var(--ink);
    margin: 0;
    line-height: 1;
  }
  .offer-line1 { top: 26px; font-size: 35px; }
  .offer-line2 { top: 78px; font-size: 39px; }
  .offer strong { font-weight: 700; font-size: 46px; }
  .pill {
    position: absolute;
    top: 164px;
    height: 147px;
    background: var(--blue);
    border: 2px solid #5d8ccc;
    border-radius: 26px;
    box-sizing: border-box;
    color: var(--white);
    text-align: center;
  }
  .schedule { left: 53px; width: 377px; font-family: "Oxygen", sans-serif; padding-top: 12px; }
  .schedule h2 { margin: 0 0 6px; font-size: 33px; font-weight: 700; line-height: 1.1; }
  .schedule p { margin: 0; font-size: 19px; font-weight: 300; line-height: 1.55; }
  .schedule b { font-weight: 700; }
  .prize { left: 447px; width: 234px; font-family: "Libre Baskerville", serif; font-weight: 700; padding-top: 10px; }
  .prize .amount { display: block; font-size: 44px; line-height: 1.05; }
  .prize .cash { display: block; font-size: 44px; line-height: 1.05; }
  .prize .note { display: block; font-size: 16px; margin-top: 8px; }
  .footer {
    position: absolute;
    left: 9px;
    top: 337px;
    width: 719px;
    height: 57px;
    background: var(--blue-deep);
    border-radius: 28px 28px 0 0;
    color: var(--white);
    font-family: "Oxygen", sans-serif;
    display: flex;
    align-items: center;
    justify-content: center;
    gap: 10px;
  }
  .footer .label { font-size: 28px; font-weight: 400; }
  .footer .url { font-size: 36px; font-weight: 400; }
</style>
</head>
<body>
  <main class="poster">
    <div class="brand-name">Drovelux Bootcamps</div>
    <h1 class="headline headline-top">Fresh Start,</h1>
    <h1 class="headline headline-bottom">Body Quest</h1>

    <svg class="hero" viewBox="0 0 737 490" role="img" aria-label="Photo of a smiling group in pink and red tops doing lunges together in a bright fitness studio">
      <defs>
        <linearGradient id="studio-tone" x1="0" y1="0" x2="0.15" y2="1">
          <stop offset="0" stop-color="#efece8"/>
          <stop offset="0.22" stop-color="#dedad6"/>
          <stop offset="0.42" stop-color="#cfc3c2"/>
          <stop offset="0.55" stop-color="#d79a9c"/>
          <stop offset="0.68" stop-color="#b8a8a0"/>
          <stop offset="0.8" stop-color="#d2ae88"/>
          <stop offset="1" stop-color="#b88a60"/>
        </linearGradient>
      </defs>
      <polygon points="0,70 241,0 491,0 737,70 737,490 0,490" fill="var(--blue)"/>
      <polygon points="0,77 241,7 491,7 737,77 737,484 0,484" fill="url(#studio-tone)"/>
    </svg>

    <section class="info">
      <p class="offer offer-line1">6 Weeks of Training, Nutrition,</p>
      <p class="offer offer-line2">and Coaching Starting at just <strong>$99!</strong></p>

      <div class="pill schedule">
        <h2>Kick Off Meeting:</h2>
        <p><b>Thursday, Jan 12th at 7:30 pm</b></p>
        <p>Start Date <b>Tuesday, January 17th</b></p>
        <p>End Date <b>Saturday, February 25th</b></p>
      </div>

      <div class="pill prize">
        <span class="amount">$500</span>
        <span class="cash">CASH</span>
        <span class="note">Prize for Winner!</span>
      </div>

      <div class="footer">
        <span class="label">For More Info</span>
        <span class="url">www.droveluxbootcamps.com</span>
      </div>
    </section>
  </main>
</body>
</html>
```